Webbanner-Design für Beratungs-, Ausbildungs- und Forschungsunternehmen
Sehr schnelle Erstellung und Anpassung des Designs. Sehr gute Arbeit!
Zielgruppe
Wir sind ein Beratungs-, Ausbildungs- und Forschungsunternehmen im Bereich der chemischen instrumentellen Analytik.
Unsere Zielgruppe sind andere Unternehmen in unserem Bereich, deren Mitarbeiter*Innen, sowie Hochschulen und Wissenschaftler.
Für eine wissenschaftliche Veranstaltung suchen wir ein Banner, das die Sichtbarkeit der Veranstaltung im Vorfeld erhöhen soll.
Aufgabenstellung
Das Webbanner soltle alle wichtigen Informationen zur Veranstaltung, sowie unser Firmenlogo enthalten (Titel, Datum, Ort, Hinweis auf mögliche Online-Teilnahme)
Ein schlichtes Design wäre wünschenswert, es darf aber gerne auffallen. Das Banner soll zur Bewerbung der Veranstaltung auf Websiten und in den sozialen Medien genutzt werden
Die Größe soll W:768 x H:90 px sein. (mit Hyperlink)

```html
<!DOCTYPE html>
<html lang="en">
<head>
<meta charset="utf-8">
<title>MS meets QSA – Web Banner</title>
<link rel="stylesheet" href="https://fonts.googleapis.com/css2?family=Poppins:wght@400;600;700&family=Roboto:wght@500&display=swap">
<style>
  :root {
    --stage-grey: #9b9b9b;
    --label-grey: #7c7c7c;
    --teal: #55d3d3;
    --ink: #111111;
    --paper: #ffffff;
  }
  html, body {
    margin: 0;
    padding: 0;
    width: 1200px;
    height: 589px;
    overflow: hidden;
    background: var(--stage-grey);
  }
  .stage {
    position: relative;
    width: 1200px;
    height: 589px;
  }
  .banner-frame {
    position: absolute;
    left: 320px;
    top: 278px;
    width: 496px;
    height: 58px;
    display: block;
    text-decoration: none;
  }
  .banner {
    position: absolute;
    left: 0;
    top: 0;
    width: 768px;
    height: 90px;
    transform: scale(0.6459);
    transform-origin: 0 0;
    background: var(--teal);
    overflow: hidden;
    color: var(--ink);
  }
  .banner-shapes {
    position: absolute;
    inset: 0;
  }
  .brand {
    position: absolute;
    left: 10px;
    top: 33px;
    display: flex;
    align-items: center;
    gap: 6px;
    font-family: "Poppins", sans-serif;
    font-weight: 600;
    font-size: 15px;
    line-height: 22px;
    color: var(--ink);
    white-space: nowrap;
  }
  .brand-dot {
    width: 10px;
    height: 10px;
    border-radius: 50%;
    background: var(--teal);
  }
  .event-title {
    position: absolute;
    left: 158px;
    width: 398px;
    top: 14px;
    margin: 0;
    text-align: center;
    font-family: "Poppins", sans-serif;
    font-weight: 700;
    font-size: 35px;
    line-height: 44px;
  }
  .event-subtitle {
    position: absolute;
    left: 158px;
    width: 398px;
    top: 54px;
    margin: 0;
    text-align: center;
    font-family: "Roboto", sans-serif;
    font-weight: 500;
    font-size: 16.5px;
    line-height: 22px;
    white-space: nowrap;
  }
  .event-date {
    position: absolute;
    left: 564px;
    width: 176px;
    top: 6px;
    margin: 0;
    text-align: center;
    font-family: "Poppins", sans-serif;
    font-weight: 600;
    font-size: 16.5px;
    line-height: 22px;
    white-space: nowrap;
  }
  .event-place {
    position: absolute;
    left: 540px;
    width: 224px;
    top: 27px;
    margin: 0;
    text-align: center;
    font-family: "Poppins", sans-serif;
    font-weight: 400;
    font-size: 13px;
    line-height: 18px;
    white-space: nowrap;
  }
  .event-place strong {
    font-weight: 600;
    font-size: 14.5px;
  }
  .cta {
    position: absolute;
    left: 571px;
    top: 47px;
    width: 172px;
    height: 38px;
    background: var(--ink);
    color: var(--paper);
    font-family: "Poppins", sans-serif;
    font-weight: 400;
    font-size: 12.5px;
    letter-spacing: -0.3px;
    display: flex;
    align-items: center;
    justify-content: center;
  }
  .size-label {
    position: absolute;
    left: 0;
    width: 1135px;
    top: 364px;
    margin: 0;
    text-align: center;
    font-family: "Poppins", sans-serif;
    font-weight: 700;
    font-size: 21px;
    color: var(--label-grey);
  }
</style>
</head>
<body>
  <div class="stage">
    <a class="banner-frame" href="#">
      <div class="banner">
        <svg class="banner-shapes" width="768" height="90" viewBox="0 0 768 90" aria-hidden="true">
          <polygon points="0,0 177,0 136,90 0,90" fill="#ffffff"/>
          <polygon points="168,0 177,0 136,90 127,90" fill="#111111"/>
        </svg>
        <div class="brand"><span class="brand-dot"></span>QUANTA-LS</div>
        <h1 class="event-title">MS meets QSA</h1>
        <p class="event-subtitle">Mass Spectrometry meets Quantitative Screening</p>
        <p class="event-date">11./12. March 2022</p>
        <p class="event-place">Halvestadt, Germany <strong>and ONLINE</strong></p>
        <div class="cta">INFO AND REGISTRATION</div>
      </div>
    </a>
    <p class="size-label">W:768 X H:90 PX</p>
  </div>
</body>
</html>
```